Rocket business card

Modern business card design, use of color is good with clean space too.

Things to include on card:

Quote: I add fuel to your optometry practice

- Eyewear Sales
- Admin Duties
- Revenue Collection
- Leadership
- Tech Adoption
- COGS Reduction
- Product Sourcing
-Medical Growth

Dalton Vesk, CEO
Lume Vantor
Text Me! 847-302-6194
dalton@lumevantor.net

```html
<!DOCTYPE html>
<html lang="en">
<head>
<meta charset="utf-8">
<title>Lume Vantor – Business Card</title>
<link rel="stylesheet" href="https://fonts.googleapis.com/css2?family=Montserrat:wght@300;400;500;700&display=swap">
<style>
  :root {
    --bg: #e9e4dd;
    --card-white: #ffffff;
    --card-black: #0c0c0c;
    --ink: #1a1a1a;
    --orange: #ea7a23;
    --orange-light: #f39a3a;
    --red-orange: #d9473f;
    --faint-mark: #2e2e2e;
    --list-text: #e8e8e8;
  }
  * { box-sizing: border-box; margin: 0; padding: 0; }
  html, body { width: 1200px; height: 859px; overflow: hidden; }
  body {
    background: var(--bg);
    font-family: "Montserrat", sans-serif;
    position: relative;
  }
  .card {
    position: absolute;
    top: 288px;
    width: 502px;
    height: 286px;
    overflow: hidden;
    box-shadow: 0 6px 14px rgba(0,0,0,0.25);
  }
  .card--front { left: 59px; background: var(--card-white); color: var(--ink); }
  .card--back { left: 639px; background: var(--card-black); }

  .decor-disc { position: absolute; top: 0; left: 0; width: 502px; height: 286px; }

  .brand {
    position: absolute;
    left: 23px;
    top: 78px;
    display: flex;
    align-items: center;
    gap: 8px;
    font-size: 22px;
    font-weight: 400;
    letter-spacing: 1px;
    color: var(--ink);
  }
  .brand__dot { width: 14px; height: 14px; border-radius: 50%; background: var(--orange); }

  .person {
    position: absolute;
    left: 24px;
    top: 146px;
    font-size: 16.5px;
    white-space: nowrap;
  }
  .person__name { color: var(--orange); font-weight: 700; letter-spacing: 0.6px; }
  .person__divider { color: var(--orange); font-weight: 500; margin: 0 3px; }
  .person__role { font-weight: 400; font-size: 14px; }

  .contact {
    position: absolute;
    left: 24px;
    top: 178px;
    font-size: 12.8px;
    line-height: 17.5px;
    list-style: none;
  }
  .contact__item { display: flex; align-items: center; gap: 6px; }
  .contact__icon { width: 12px; height: 12px; flex: none; }
  .contact__label { color: var(--orange); }

  .tagline {
    position: absolute;
    left: 23px;
    top: 229px;
    font-size: 13px;
    line-height: 16px;
    letter-spacing: 1.1px;
    text-transform: uppercase;
    font-weight: 400;
  }

  .back-mark {
    position: absolute;
    left: 222px;
    top: 22px;
    font-size: 22px;
    font-weight: 400;
    letter-spacing: 1px;
    color: var(--faint-mark);
  }
  .back-rule {
    position: absolute;
    left: 222px;
    top: 79px;
    width: 1px;
    height: 127px;
    background: var(--orange);
  }
  .services {
    position: absolute;
    left: 276px;
    top: 76px;
    list-style: none;
    color: var(--list-text);
    font-size: 13.6px;
    font-weight: 300;
    line-height: 16.9px;
    letter-spacing: 0.3px;
  }
</style>
</head>
<body>
  <section class="card card--front">
    <svg class="decor-disc" viewBox="0 0 502 286" role="img" aria-label="Large brand decoration area">
      <defs>
        <linearGradient id="discFront" x1="0" y1="0" x2="1" y2="1">
          <stop offset="0" stop-color="var(--red-orange)"/>
          <stop offset="1" stop-color="var(--orange-light)"/>
        </linearGradient>
      </defs>
      <circle cx="541" cy="142" r="204" fill="url(#discFront)"/>
    </svg>

    <div class="brand"><span class="brand__dot"></span><span>LUME VANTOR</span></div>

    <p class="person">
      <span class="person__name">DALTON VESK</span><span class="person__divider">|</span><span class="person__role">CEO</span>
    </p>

    <ul class="contact">
      <li class="contact__item">
        <svg class="contact__icon" viewBox="0 0 24 24" fill="none" stroke="var(--red-orange)" stroke-width="2">
          <path d="M5 3h4l2 5-2.5 1.5a11 11 0 0 0 6 6L16 13l5 2v4a2 2 0 0 1-2 2A16 16 0 0 1 3 5a2 2 0 0 1 2-2z"/>
        </svg>
        <span><span class="contact__label">Text Me!</span> 847-302-6194</span>
      </li>
      <li class="contact__item">
        <svg class="contact__icon" viewBox="0 0 24 24" fill="none" stroke="var(--red-orange)" stroke-width="2">
          <rect x="2" y="5" width="20" height="14"/>
          <path d="M2 5l10 8 10-8"/>
        </svg>
        <span>dalton@lumevantor.net</span>
      </li>
    </ul>

    <p class="tagline">I add fuel to your<br>optometry practice</p>
  </section>

  <section class="card card--back">
    <svg class="decor-disc" viewBox="0 0 502 286" role="img" aria-label="Large brand decoration area">
      <defs>
        <linearGradient id="discBack" x1="0" y1="0" x2="1" y2="1">
          <stop offset="0" stop-color="var(--orange-light)"/>
          <stop offset="1" stop-color="var(--red-orange)"/>
        </linearGradient>
      </defs>
      <circle cx="-39" cy="142" r="204" fill="url(#discBack)"/>
    </svg>

    <div class="back-mark">LUME VANTOR</div>
    <div class="back-rule"></div>
    <ul class="services">
      <li>Eyewear Sales</li>
      <li>Admin Duties</li>
      <li>Revenue Collection</li>
      <li>Leadership</li>
      <li>Tech Adoption</li>
      <li>COGS Reduction</li>
      <li>Product Sourcing</li>
      <li>Medical Growth</li>
    </ul>
  </section>
</body>
</html>
```